New IT Consulting Company needs new Branding

I need some business cards and logo created for new IT consulting company called Cobaltwave Partners Pty Ltd.

We deal with enterprise IT solution and IT consulting Firm.
Assisting businesses with Technology Upgrades and System integration

We have no existing color schemes in mind but after something a little recognizable but elegant also.

We are looking for something that conveys a professional look.

Target Market(s)

Targeting small to medium businesses with 0-500 employees

Industry/Entity Type

Information Technology

Contact Information for Business Card

Name, Title , Mobile Contact, Phone Contact , Email and Website URL

Logo Text

Cobaltwave Pty Ltd "Building IT Solutions the right way"

Font styles to use
Serif
Sans Serif

Requirements
Nice to have
• Looking for one or two primary colors and sticking to geometric or symmetrical design for the logo

```html
<!DOCTYPE html>
<html lang="en">
<head>
<meta charset="utf-8">
<title>Cobaltwave Partners – Business Card</title>
<link href="https://fonts.googleapis.com/css2?family=Open+Sans:wght@400;600;700&display=swap" rel="stylesheet">
<style>
  :root {
    --backdrop: #d8d5d1;
    --card: #eef0f1;
    --ink: #3a3f45;
    --cobalt: #1f5a8c;
    --band-blue: #1d4f7c;
    --band-dark: #16181b;
    --icon: #2a4c6e;
    --address: #a9bccd;
    --brand: #1c2e44;
  }
  * { margin: 0; padding: 0; box-sizing: border-box; }
  html, body { width: 1200px; height: 970px; overflow: hidden; }
  body {
    background: var(--backdrop);
    font-family: "Open Sans", Arial, sans-serif;
    position: relative;
  }
  .card {
    position: absolute;
    left: 100px; top: 201px;
    width: 1000px; height: 567px;
    background: linear-gradient(135deg, #f4f5f6 0%, var(--card) 55%, #e4e7ea 100%);
    overflow: hidden;
    box-shadow: 0 10px 30px rgba(0,0,0,0.18);
  }
  .card-art { position: absolute; inset: 0; width: 1000px; height: 567px; }
  .holder-name {
    position: absolute; left: 54px; top: 100px;
    font-size: 40px; font-weight: 700; color: var(--cobalt); line-height: 1;
  }
  .holder-title {
    position: absolute; left: 56px; top: 150px;
    font-size: 25px; font-weight: 400; color: var(--ink); line-height: 1;
  }
  .contacts { position: absolute; left: 54px; top: 264px; list-style: none; }
  .contacts li {
    display: flex; align-items: center; height: 35.5px;
    font-size: 25px; color: var(--ink);
  }
  .contacts svg { width: 20px; height: 20px; margin-right: 12px; flex: none; fill: var(--icon); }
  .brand {
    position: absolute; left: 467px; top: 70px; width: 400px;
    text-align: center; color: var(--brand);
    font-weight: 600; font-size: 40px; line-height: 1.15;
  }
  .brand-dot {
    display: block; width: 120px; height: 120px; margin: 0 auto 30px;
    border-radius: 50%; background: var(--brand);
  }
  .address {
    position: absolute; left: 0; right: 0; top: 530px;
    text-align: center; font-size: 24px; color: var(--address); line-height: 1;
  }
</style>
</head>
<body>
  <div class="card">
    <svg class="card-art" viewBox="0 0 1000 567" aria-hidden="true">
      <circle cx="0" cy="130" r="38" fill="#2a2c2f"/>
      <path d="M0 435 Q430 525 1000 370 L1000 412 Q430 545 0 470 Z" fill="var(--band-dark)"/>
      <path d="M0 470 Q430 545 1000 412 L1000 567 L0 567 Z" fill="var(--band-blue)"/>
    </svg>

    <h1 class="holder-name">Marcus Ellery</h1>
    <p class="holder-title">Managing Member</p>

    <ul class="contacts">
      <li><svg viewBox="0 0 24 24"><path d="M6.6 10.8a15.1 15.1 0 0 0 6.6 6.6l2.2-2.2a1 1 0 0 1 1-.25 11.4 11.4 0 0 0 3.6.57 1 1 0 0 1 1 1V20a1 1 0 0 1-1 1A17 17 0 0 1 3 4a1 1 0 0 1 1-1h3.5a1 1 0 0 1 1 1c0 1.25.2 2.45.57 3.57a1 1 0 0 1-.25 1z"/></svg>(916) 555-0142</li>
      <li><svg viewBox="0 0 24 24"><path d="M7 3h8l2 2v4H7z M4 10h16a1 1 0 0 1 1 1v7h-3v3H6v-3H3v-7a1 1 0 0 1 1-1z M8 16v3h8v-3z"/></svg>(916) 555-0143</li>
      <li><svg viewBox="0 0 24 24"><path d="M8 2h8a2 2 0 0 1 2 2v16a2 2 0 0 1-2 2H8a2 2 0 0 1-2-2V4a2 2 0 0 1 2-2zm0 3v13h8V5zm4 14.2a1 1 0 1 0 0 .01z"/></svg>(530) 555-0178</li>
      <li><svg viewBox="0 0 24 24"><path d="M3 6h18v12H3z M3 6l9 7 9-7" fill="none" stroke="var(--icon)" stroke-width="0"/><path d="M3 7.5l9 6.5 9-6.5V18H3z M3 6h18l-9 6.5z"/></svg>marcus@cobaltwave.com</li>
      <li><svg viewBox="0 0 24 24"><path d="M12 2a10 10 0 1 0 0 20 10 10 0 0 0 0-20zm6.9 6h-3a15 15 0 0 0-1.3-3.9A8 8 0 0 1 18.9 8zM12 4c.8 1.1 1.5 2.5 1.9 4h-3.8c.4-1.5 1.1-2.9 1.9-4zM4.3 14a8 8 0 0 1 0-4h3.4a16 16 0 0 0 0 4zm.8 2h3a15 15 0 0 0 1.3 3.9A8 8 0 0 1 5.1 16zm3-8h-3a8 8 0 0 1 4.3-3.9A15 15 0 0 0 8.1 8zM12 20c-.8-1.1-1.5-2.5-1.9-4h3.8c-.4 1.5-1.1 2.9-1.9 4zm2.3-6H9.7a14 14 0 0 1 0-4h4.6a14 14 0 0 1 0 4zm.3 5.9a15 15 0 0 0 1.3-3.9h3a8 8 0 0 1-4.3 3.9zm1.7-5.9a16 16 0 0 0 0-4h3.4a8 8 0 0 1 0 4z"/></svg>www.cobaltwave.com</li>
    </ul>

    <div class="brand">
      <span class="brand-dot"></span>
      Cobaltwave Partners<br>Pty Ltd
    </div>

    <p class="address">1187 Harbor Point Way, Sacramento, CA 95833</p>
  </div>
</body>
</html>
```